k eLiquid Label

We are an electronic cigarette eLiquid manufacturer with an outdated label design which needs to be updated and become more modern. All information listed on the label cannot be changed or removed.

There are 4 colour coding on the labels that cannot change.
0mg is white
12mg is yellow
18mg is blue
24mg is red

We prefer a blue type background however are not committed to it with the proper design however if a new colour is chosen it must compliment the colour band for each colour coding

The "dots" on the front of the bottle need to be larger.

The "V" on the front needs to be in this font however we can accept slight changes to it for effect.

Issues we are facing:
The 0mg and the 18mg look too close in colour and need to be completely different in colouring.

The background colouring is too dark and you cannot see the 50/50 in the watermark.

Reason: We have not received a design which is suitable to our needs. We have see a few close ones however not exact. Thanks

Reason: I was forced to go out of country for a family emergency and to be fair I am extending the deadline

```html
<!DOCTYPE html>
<html lang="en">
<head>
<meta charset="utf-8">
<title>k eLiquid Label – 12mg</title>
<link href="https://fonts.googleapis.com/css2?family=Anton&family=Arimo:wght@400;700&family=Roboto+Slab:wght@800&family=Titillium+Web:wght@900&family=Noto+Serif&display=swap" rel="stylesheet">
<style>
  :root {
    --band-yellow: #fff200;
    --ink: #0b0b0b;
    --paper: #ffffff;
    --sky-light: #e8f1f6;
    --sky-mid: #a9cfe0;
    --sky-deep: #5ea9c6;
    --steel: #8d9aa2;
    --night: #141414;
    --heading-yellow: #ffe81a;
    --dot-white: #f2f2f2;
    --dot-blue: #241f63;
    --dot-red: #e8262b;
    --ring: #b9b9b9;
  }
  * { box-sizing: border-box; margin: 0; padding: 0; }
  html, body { width: 1200px; height: 900px; overflow: hidden; background: var(--paper); }
  .canvas { position: relative; width: 1200px; height: 900px; }

  .label { position: absolute; left: 68px; top: 173px; width: 1072px; height: 419px; border: 1.5px solid var(--ink); overflow: hidden; }

  .band { position: absolute; left: 0; width: 100%; height: 34px; background: var(--band-yellow);
    display: flex; justify-content: space-between; align-items: center; padding: 0 6px;
    font-family: "Titillium Web", sans-serif; font-weight: 900; font-size: 22px; letter-spacing: 3px; color: var(--ink); z-index: 3; }
  .band--top { top: 0; border-bottom: 1.5px solid var(--ink); }
  .band--bottom { bottom: 0; border-top: 1.5px solid var(--ink); padding: 0 6px; }

  .panel-info { position: absolute; left: 0; top: 34px; width: 284px; height: 351px;
    background: linear-gradient(90deg, var(--paper) 20%, var(--sky-light) 60%, var(--sky-mid)); }
  .panel-brand { position: absolute; left: 284px; top: 34px; width: 500px; height: 351px;
    background: linear-gradient(90deg, var(--sky-mid), var(--sky-deep) 55%, #7fb6cc 85%, #9aa4a8); }
  .panel-warning { position: absolute; left: 782px; top: 34px; width: 290px; height: 351px;
    background: linear-gradient(90deg, #8d9396 0%, #4a4d4f 45%, var(--night) 100%); }
  .smoke { position: absolute; left: 720px; top: 120px; width: 352px; height: 260px;
    background: radial-gradient(ellipse at 40% 60%, rgba(235,240,242,.55), rgba(200,210,215,.2) 45%, transparent 70%); }

  .heading { font-family: "Anton", sans-serif; color: var(--heading-yellow); letter-spacing: .3px;
    text-shadow: -1px -1px 0 var(--ink), 1px -1px 0 var(--ink), -1px 1px 0 var(--ink), 1px 1px 0 var(--ink); text-transform: uppercase; }

  .ingredients-title { position: absolute; left: 13px; top: 82px; font-size: 25px; }
  .ingredients { position: absolute; left: 13px; top: 120px; width: 254px; font-family: "Arimo", sans-serif;
    font-weight: 700; font-size: 13.6px; line-height: 17.4px; text-align: justify; color: var(--ink); }
  .producer { position: absolute; left: 18px; top: 256px; width: 250px; font-family: "Arimo", sans-serif;
    font-weight: 700; font-size: 12.6px; line-height: 16px; color: var(--ink); }
  .producer .centered { text-align: center; display: block; }
  .producer .address { display: block; margin-top: 7px; font-size: 13.4px; line-height: 17px; }
  .batch-box { position: absolute; left: 14px; top: 328px; width: 255px; height: 45px; background: var(--paper);
    border: 1px solid #cfd6da; padding: 6px 12px; font-family: "Arimo", sans-serif; font-size: 11px; line-height: 14px; color: #222; }

  .strip { position: absolute; top: 36px; width: 62px; height: 320px; background: var(--ink);
    display: flex; align-items: center; justify-content: center; }
  .strip span { writing-mode: vertical-rl; font-family: "Roboto Slab", serif; font-weight: 800; font-size: 34px; color: var(--paper); }
  .strip--one { left: 305px; }
  .strip--two { left: 373px; }

  .brand-name { position: absolute; left: 452px; top: 126px; font-family: "Anton", sans-serif; font-size: 60px;
    color: var(--ink); line-height: 1; }
  .brand-name-mark { position: absolute; left: 474px; top: 70px; width: 44px; height: 44px; border-radius: 50%; background: var(--ink); }

  .volume { position: absolute; left: 630px; top: 266px; font-family: "Anton", sans-serif; font-size: 22px; color: var(--ink); }
  .strength-dot { position: absolute; left: 552px; top: 228px; width: 68px; height: 68px; }

  .ratio-marks { position: absolute; left: 636px; top: 36px; width: 140px; }
  .ratio { height: 78px; margin-bottom: 8px; border: 3px solid rgba(200,215,222,.45); border-radius: 6px;
    display: flex; align-items: center; justify-content: center;
    font-family: "Arimo", sans-serif; font-weight: 700; font-size: 42px; color: rgba(200,215,222,.45); }

  .notice { position: absolute; left: 300px; top: 362px; font-family: "Noto Serif", serif; font-size: 12.4px; color: #e8f1f5; }

  .hazard-icon { position: absolute; left: 850px; top: 38px; width: 40px; height: 40px; }
  .warn-title { position: absolute; font-size: 22px; }
  .warn-title--fr { left: 914px; top: 44px; }
  .warn-title--en { left: 798px; top: 150px; }
  .warn-title--poison { left: 918px; top: 248px; }
  .warn-text { position: absolute; left: 800px; width: 246px; font-family: "Arimo", sans-serif; font-weight: 700;
    font-size: 13px; line-height: 16.3px; color: #f4f4f4; text-align: justify; }
  .warn-text--fr { top: 82px; }
  .warn-text--en { top: 186px; }
  .warn-text--poison { top: 282px; }

  .variants { position: absolute; left: 824px; top: 614px; display: flex; gap: 8px; }
  .variants svg { width: 82px; height: 82px; }
</style>
</head>
<body>
<div class="canvas">
  <div class="label">
    <div class="band band--top">
      <span>12mg/ml</span><span>12mg/ml</span><span>12mg/ml</span><span>12mg/ml</span><span>12mg/ml</span><span>12mg/ml</span><span>12mg/ml</span><span>12mg/ml</span>
    </div>

    <div class="panel-info"></div>
    <div class="panel-brand"></div>
    <div class="panel-warning"></div>
    <div class="smoke" role="img" aria-label="Soft drifting vapour cloud"></div>

    <h2 class="heading ingredients-title">Ingrédients</h2>
    <p class="ingredients">Propyléne Glycol, Glycérine, Alcool de Qualitié Alimentaire, Arômes Naturel et Artificiels.<br>Propylene Glycol, Vegetable Glycerine, Food Grade Alcohol, Natural and Artificial Flavours.</p>
    <p class="producer"><span class="centered">Produit et emballlé exclusivement pour:<br>Produce and Packaged exclusively for:</span><span class="address">4419027 Canada Inc, Lakeview ON, K0A 1B0</span></p>
    <div class="batch-box">BATCH:<br>EXPIRES:</div>

    <div class="strip strip--one"><span>E-Liquid</span></div>
    <div class="strip strip--two"><span>E-Liquid</span></div>

    <div class="ratio-marks">
      <div class="ratio">50/50</div><div class="ratio">50/50</div><div class="ratio">50/50</div><div class="ratio">50/50</div>
    </div>

    <div class="brand-name-mark"></div>
    <div class="brand-name">k eLiquid</div>

    <svg class="strength-dot" viewBox="0 0 68 68" aria-label="12mg">
      <circle cx="34" cy="34" r="33" fill="var(--ring)"/>
      <circle cx="34" cy="34" r="26" fill="var(--band-yellow)"/>
      <text x="34" y="42" text-anchor="middle" font-family="Anton, sans-serif" font-size="22" fill="var(--ink)" transform="rotate(-15 34 34)">12mg</text>
    </svg>
    <div class="volume">30ml</div>

    <p class="notice">Product contains nicotine. Must be 18+ to purchase and consume.</p>

    <svg class="hazard-icon" viewBox="0 0 40 40" aria-hidden="true">
      <polygon points="12,1 28,1 39,12 39,28 28,39 12,39 1,28 1,12" fill="#6f6f6f" stroke="#222" stroke-width="2"/>
      <circle cx="20" cy="17" r="7" fill="var(--ink)"/>
      <rect x="16" y="22" width="8" height="5" fill="var(--ink)"/>
      <path d="M9 27 L31 33 M31 27 L9 33" stroke="var(--ink)" stroke-width="3"/>
    </svg>
    <h3 class="heading warn-title warn-title--fr">Contenir nocif</h3>
    <p class="warn-text warn-text--fr">Ne pas avaler. Ne pas mettre dans les yeux ou sur la peau ou les vétements. Tenis hors de portée des enfants et des animaux.</p>
    <h3 class="heading warn-title warn-title--en">Warning contents harmful</h3>
    <p class="warn-text warn-text--en">Do not swallow. Do not get in eyes or on skin or clothing. Keep out of reach of children and pets.</p>
    <h3 class="heading warn-title warn-title--poison">Danger poison</h3>
    <p class="warn-text warn-text--poison">En cas d’ingestion consulter centre antipoison ou un médecin immédiatement. Peux contenir de noix.<br>If swallowed consult poison control centre or a doctor immediately. May contain nuts.</p>

    <div class="band band--bottom">
      <span>DANGER POISON</span><span>DANGER POISON</span><span>DANGER POISON</span><span>DANGER POISON</span><span>DANGER POISON</span>
    </div>
  </div>

  <div class="variants">
    <svg viewBox="0 0 82 82" aria-label="Zero nicotine">
      <circle cx="41" cy="41" r="40" fill="var(--ring)"/>
      <circle cx="41" cy="41" r="32" fill="var(--dot-white)"/>
      <text x="41" y="46" text-anchor="middle" font-family="Anton, sans-serif" font-size="26" fill="var(--paper)" stroke="var(--ink)" stroke-width="1.2" transform="rotate(-15 41 41)">zero</text>
      <text x="46" y="62" text-anchor="middle" font-family="Arimo, sans-serif" font-weight="700" font-size="8" fill="var(--ink)" transform="rotate(-15 41 41)">nicotine</text>
    </svg>
    <svg viewBox="0 0 82 82" aria-label="18mg">
      <circle cx="41" cy="41" r="40" fill="var(--ring)"/>
      <circle cx="41" cy="41" r="32" fill="var(--dot-blue)"/>
      <text x="41" y="50" text-anchor="middle" font-family="Anton, sans-serif" font-size="26" fill="var(--paper)" stroke="var(--ink)" stroke-width="1" transform="rotate(-15 41 41)">18mg</text>
    </svg>
    <svg viewBox="0 0 82 82" aria-label="24mg">
      <circle cx="41" cy="41" r="40" fill="var(--ring)"/>
      <circle cx="41" cy="41" r="32" fill="var(--dot-red)"/>
      <text x="41" y="50" text-anchor="middle" font-family="Anton, sans-serif" font-size="26" fill="var(--paper)" stroke="var(--ink)" stroke-width="1" transform="rotate(-15 41 41)">24mg</text>
    </svg>
  </div>
</div>
</body>
</html>
```